Business Card Design Project

Branding and Marketing Company

Target Market(s)

Lifestyle Brands. Velo, Quint, Halden Crest

Industry/Entity Type

Business

Contact Information for Business Card

I'm looking for a sleek design that is simple yet stands out. I would like to see some embossed options and even metallic features. I am looking for a black and white theme business card. Our company font is Avenir (Regular, Italic, Bold) I would like to have just the logo and the following slogan on the back of card.CREATING THE NEXT BIG THING IN HEALTH & WELLNESS

```html
<!DOCTYPE html>
<html lang="en">
<head>
<meta charset="utf-8">
<title>Lumen Works — Business Card</title>
<link href="https://fonts.googleapis.com/css2?family=Nunito+Sans:ital,wght@0,300;0,400;0,600;1,400&display=swap" rel="stylesheet">
<style>
  :root {
    --backdrop: #e9e4dc;
    --card-white: #ffffff;
    --card-black: #0b0b0b;
    --ink: #4a4a48;
    --ink-soft: #6b6b68;
    --silver: #c9c7c2;
    --silver-dim: #a8a6a1;
  }
  * { margin: 0; padding: 0; box-sizing: border-box; }
  html, body {
    width: 1200px; height: 1200px; overflow: hidden;
    background: var(--backdrop);
    font-family: "Nunito Sans", "Avenir", sans-serif;
  }
  .canvas { position: relative; width: 1200px; height: 1200px; }

  .card {
    position: absolute; left: 286px; width: 628px; height: 390px;
  }
  .card--front { top: 150px; background: var(--card-white); }
  .card--back { top: 681px; background: var(--card-black); }

  /* Front */
  .identity {
    position: absolute; left: 31px; top: 42px;
    border-left: 2px solid var(--ink); padding-left: 7px;
    color: var(--ink);
  }
  .identity__name { font-size: 25px; font-weight: 400; letter-spacing: 0.5px; line-height: 1.1; }
  .identity__title { font-size: 17px; font-weight: 400; line-height: 1.3; }

  .contact-list { position: absolute; left: 36px; top: 214px; list-style: none; color: var(--ink); }
  .contact-list__item {
    display: flex; align-items: flex-start; gap: 12px;
    font-size: 15px; line-height: 21px; margin-bottom: 8px;
  }
  .contact-list__icon { width: 14px; height: 14px; margin-top: 4px; flex: none; fill: var(--ink-soft); }

  .wordmark {
    position: absolute; left: 408px; top: 168px; width: 190px;
    text-align: center; color: var(--ink);
    font-size: 34px; font-weight: 400; letter-spacing: 2px; line-height: 1;
  }

  /* Back */
  .back-wordmark {
    position: absolute; left: 0; right: 0; top: 218px;
    text-align: center; color: var(--silver);
    font-size: 40px; font-weight: 400; letter-spacing: 2px; line-height: 1;
  }
  .back-mark {
    position: absolute; left: 304px; top: 150px;
    width: 20px; height: 20px; border-radius: 50%; background: var(--silver);
  }
  .slogan {
    position: absolute; left: 0; right: 0; top: 326px;
    text-align: center; color: var(--silver-dim);
    font-size: 17px; font-weight: 400; letter-spacing: 0.3px;
  }
  .slogan em { font-style: italic; }
</style>
</head>
<body>
<main class="canvas">
  <section class="card card--front" aria-label="Business card front">
    <div class="identity">
      <p class="identity__name">Your Name</p>
      <p class="identity__title">Job Title</p>
    </div>

    <ul class="contact-list">
      <li class="contact-list__item">
        <svg class="contact-list__icon" viewBox="0 0 16 16" aria-hidden="true"><path d="M1 5c0-2 3-3 7-3s7 1 7 3v1h-4V5H5v1H1zM4 7h8l2 7H2z"/></svg>
        <span>000 000 0000</span>
      </li>
      <li class="contact-list__item">
        <svg class="contact-list__icon" viewBox="0 0 16 16" aria-hidden="true"><path d="M1 3h14v10H1zM2 4l6 5 6-5v-0.5H2z" fill-rule="evenodd"/></svg>
        <span>youremail@XYZ.com</span>
      </li>
      <li class="contact-list__item">
        <svg class="contact-list__icon" viewBox="0 0 16 16" aria-hidden="true"><path d="M8 1a7 7 0 1 0 0 14A7 7 0 0 0 8 1zm0 1.3c.8 0 1.8 1.9 2 4.7H6c.2-2.8 1.2-4.7 2-4.7zM2.4 7h2.4c0-1.8.4-3.3.9-4.2A5.7 5.7 0 0 0 2.4 7zm8.8 0h2.4a5.7 5.7 0 0 0-3.3-4.2c.5.9.9 2.4.9 4.2zM2.4 9a5.7 5.7 0 0 0 3.3 4.2c-.5-.9-.9-2.4-.9-4.2zm3.6 0c.2 2.8 1.2 4.7 2 4.7s1.8-1.9 2-4.7zm5.2 0c0 1.8-.4 3.3-.9 4.2A5.7 5.7 0 0 0 13.6 9z"/></svg>
        <span>www.yourwebsite.com</span>
      </li>
      <li class="contact-list__item">
        <svg class="contact-list__icon" viewBox="0 0 16 16" aria-hidden="true"><path d="M8 0a5 5 0 0 0-5 5c0 4 5 11 5 11s5-7 5-11a5 5 0 0 0-5-5zm0 7a2 2 0 1 1 0-4 2 2 0 0 1 0 4z"/></svg>
        <span>000, Street name, Anywhere<br>City, State 0000</span>
      </li>
    </ul>

    <p class="wordmark">Lumen Works</p>
  </section>

  <section class="card card--back" aria-label="Business card back">
    <span class="back-mark" aria-hidden="true"></span>
    <p class="back-wordmark">Lumen Works</p>
    <p class="slogan">CREATING THE NEXT BIG THING IN <em>HEALTH &amp; WELLNESS</em></p>
  </section>
</main>
</body>
</html>
```